Palvanor Lending. Website design for a mortgage company.

We need a simple, but classy and artistic website design. The website should contain a home page, about page, and information page. I would like the design for each page created and I can add the content.

Palvanor Lending is a retail mortgage broker business specially crafted to provide simple, transparent, and comprehensive mortgage solutions. We understand the complexities of mortgage acquisition and have aligned with the best partners and resources to analyze the information and deliver precise, transparent, efficient, and reliable results.

Target Market(s)

We are targeting people ages 30-65 within the United States, both male and female. We are also targeting business owners and property investors specifically.

Industry/Entity Type

Mortgage Brokerage

Coding

Coded - Design and coding required

Number of Pages Required

5+ page

Font styles to use
Sans Serif
Script

Requirements
Must have
• The main purpose of this website is to provide clients with the necessary information to want to move forward with a loan transaction. The website will be informational to promote the company and showcase our purpose. The company purpose is to provide efficient and comprehensive service to clients, and to help them navigate the challenging mortgage world.

The website must mimic that of the major fortune 500 companies. It needs to be super clean, but very modern. The pictures should be of families with brown skin mostly.

The website needs to be mobile responsive. Each page needs to consist of large and responsive Hero Images. There will be background videos on the product and process pages of the website.

The website must have a semi-flat design.
The website must have a Hamburger Menu instead of a visible navigation menu.

Use the script font styles for the headlines and the sans serif for body text.

We need to have the following pages:
Home

Products

Process

About

Contact - I want a map of our office location and region. We are located in Calverdale MD and our region consists of the following states: Florida, Texas, Virginia, Maryland, and Washington DC.

```html
<!DOCTYPE html>
<html lang="en">
<head>
<meta charset="utf-8">
<title>Palvanor Lending – Mortgage Brokerage</title>
<link rel="stylesheet" href="https://fonts.googleapis.com/css2?family=Montserrat:ital,wght@0,400;0,500;0,600;0,700;1,500&family=Pinyon+Script&display=swap">
<style>
:root{
  --blue:#0f6cc0;
  --blue-bright:#1e8fe0;
  --blue-dark:#0b4f97;
  --ink:#1d1d1f;
  --text:#444;
  --muted:#777;
  --line:#dde3ea;
  --white:#fff;
  --soft:#f4f7fb;
  --script:"Pinyon Script", cursive;
  --sans:"Montserrat", sans-serif;
}
*{margin:0;padding:0;box-sizing:border-box}
html,body{width:1200px;height:3682px;overflow:hidden}
body{position:relative;background:var(--white);font-family:var(--sans);color:var(--ink)}
.abs{position:absolute}
.script-title{position:absolute;left:0;width:1200px;text-align:center;font-family:var(--script);font-size:58px;line-height:1;color:var(--ink)}
.title-rule{position:absolute;left:580px;width:40px;height:3px;background:var(--blue)}

/* header */
.site-header{position:absolute;left:0;top:0;width:1200px;height:80px;background:var(--white);z-index:3}
.contact-chip{position:absolute;top:17px;display:flex;align-items:center;gap:10px}
.contact-chip .label{font-size:11px;font-weight:600;color:var(--blue);letter-spacing:.3px}
.contact-chip .value{font-size:14px;font-weight:500;color:var(--ink)}
.brand-badge{position:absolute;left:530px;top:-10px;width:140px;height:140px;border-radius:50%;background:var(--white);display:flex;align-items:center;justify-content:center;text-align:center;box-shadow:0 4px 10px rgba(0,0,0,.12);z-index:4}
.brand-badge span{font-size:17px;font-weight:700;color:var(--blue);line-height:1.15;margin-top:22px}
.menu-btn{position:absolute;left:1012px;top:18px;width:36px;height:36px;border:2px solid var(--blue);border-radius:50%}
.menu-btn i{position:absolute;left:10px;width:12px;height:2px;background:var(--blue)}

/* hero */
.hero{position:absolute;left:0;top:80px;width:1200px;height:575px;overflow:hidden}
.hero-photo{position:absolute;inset:0;background:linear-gradient(100deg,#3d4650 0%,#5a5f62 30%,#8a8e8a 55%,#b8c2c4 80%,#d8dfe0 100%)}
.hero-copy{position:absolute;left:162px;top:150px;width:460px;color:var(--white)}
.hero-copy .script{font-family:var(--script);font-size:52px;line-height:1}
.hero-copy h1{font-size:35px;font-weight:700;margin-top:6px;letter-spacing:.3px}
.hero-copy p{font-size:15px;line-height:25px;margin-top:12px}
.btn-pill{display:inline-flex;align-items:center;gap:6px;background:var(--blue-bright);color:var(--white);font-size:14px;font-weight:600;border-radius:22px;padding:11px 16px;margin-top:20px;letter-spacing:.3px}

/* process */
.process-step{position:absolute;top:796px;width:240px;text-align:center}
.step-visual{position:relative;height:130px}
.step-num{position:absolute;top:0;font-size:118px;font-weight:700;color:var(--blue);line-height:130px;letter-spacing:-6px}
.step-ring{position:absolute;top:3px;width:124px;height:124px;border:5px solid var(--blue);border-radius:50%;background:var(--white);display:flex;align-items:center;justify-content:center}
.step-ring .core{width:104px;height:104px;border-radius:50%;background:var(--blue);display:flex;align-items:center;justify-content:center}
.step-label{font-size:17px;font-weight:600;margin-top:16px}

/* products */
.products{position:absolute;left:0;top:1044px;width:1200px;height:592px;background:linear-gradient(90deg,#1a6fbf 0%,#1878cc 50%,#2a93e0 100%)}
.products .script-title{color:var(--white)}
.products .title-rule{background:var(--white)}
.product-card{position:absolute;top:160px;width:262px;height:350px;background:var(--white);border-radius:3px;overflow:hidden;text-align:center}
.product-photo{height:182px}
.product-card h3{font-size:16px;font-weight:600;margin-top:20px}
.product-card .rule{width:32px;height:2px;background:var(--blue);margin:10px auto 0}
.product-card p{font-size:13px;line-height:20px;color:var(--text);margin:14px 20px 0}
.product-card a{display:block;font-size:13px;font-weight:600;color:var(--blue);margin-top:10px;text-decoration:none}

/* calculator */
.calc-card{position:absolute;left:162px;top:1810px;width:876px;height:310px;background:var(--white);border-radius:8px;box-shadow:0 4px 22px rgba(20,50,90,.12)}
.field-label{position:absolute;font-size:13px;font-weight:500}
.field-value{position:absolute;font-size:18px;font-weight:500}
.track{position:absolute;left:30px;width:453px;height:4px;border-radius:2px;background:var(--line)}
.track .fill{height:4px;border-radius:2px;background:var(--blue)}
.track .knob{position:absolute;top:-4px;width:12px;height:12px;border-radius:50%;background:var(--blue)}
.calc-divider{position:absolute;left:540px;top:30px;height:255px;border-left:1px dashed #c9d3de}
.payment-ring{position:absolute;left:655px;top:32px;width:118px;height:118px;border:3px solid var(--blue);border-radius:50%;text-align:center;padding-top:30px}
.payment-ring strong{display:block;font-size:23px;font-weight:700}
.payment-ring span{font-size:16px;color:var(--blue)}
.breakdown{position:absolute;left:570px;top:170px;width:265px;list-style:none}
.breakdown li{display:flex;justify-content:space-between;font-size:14px;height:31.5px;align-items:center}
.breakdown li span{position:relative;padding-left:16px}
.breakdown li span::before{content:"";position:absolute;left:0;top:5px;width:6px;height:6px;border-radius:50%;background:var(--blue)}
.breakdown li b{width:70px;font-weight:600}

/* region */
.region{position:absolute;left:0;top:2208px;width:1200px;height:400px}
.region-map{position:absolute;inset:0;background:linear-gradient(120deg,#cfcfcf 0%,#e8e8e8 40%,#dedede 70%,#c6c6c6 100%)}
.region-panel{position:absolute;left:162px;top:0;width:246px;height:319px;background:var(--white);padding:28px 14px 0 20px}
.region-panel h2{font-size:16.5px;font-weight:500;line-height:23px;color:var(--blue)}
.region-panel ul{list-style:none;margin-top:28px}
.region-panel li{font-size:14px;height:30px;display:flex;align-items:center;gap:14px}
.region-panel li i{width:13px;height:13px;border:2px solid var(--blue);border-radius:50%;position:relative}
.region-panel li i::after{content:"";position:absolute;left:2.5px;top:2.5px;width:4px;height:4px;border-radius:50%;background:var(--blue)}

/* reviews */
.review-card{position:absolute;left:240px;top:2765px;width:752px;height:290px;background:var(--white);border-radius:60px 60px 0 60px;box-shadow:0 6px 24px rgba(20,50,90,.10)}
.review-photo{position:absolute;left:190px;top:2858px;width:97px;height:97px;border:3px solid var(--white);box-shadow:0 0 0 1px #ddd;background:linear-gradient(160deg,#7aa8c8,#b9806a 55%,#a5243a)}
.review-quote{position:absolute;left:325px;top:2860px;width:633px;font-size:12.3px;line-height:20.5px;color:var(--text);text-align:justify}
.review-author{position:absolute;left:656px;top:3001px;font-size:16px;font-style:italic;font-weight:500}
.dot{position:absolute;left:1068px;width:9px;height:9px;border-radius:50%;background:#cfd5dc}

/* cta */
.cta{position:absolute;left:0;top:3142px;width:1200px;height:274px;background:linear-gradient(90deg,#1669bd 0%,#1e82d6 55%,#2a95e2 100%);color:var(--white);text-align:center}
.cta p{position:absolute;left:150px;top:66px;width:900px;font-size:19px;line-height:33px}
.cta-phone{position:absolute;left:504px;top:155px;width:193px;height:41px;background:var(--white);border-radius:21px;display:flex;align-items:center;justify-content:center;gap:8px;color:var(--ink);font-size:16px;font-weight:600}

/* footer */
.footer-nav{position:absolute;left:0;top:3446px;width:1200px;display:flex;justify-content:center;gap:52px;font-size:14px;font-weight:500;letter-spacing:.3px}
.footer-rule{position:absolute;left:162px;top:3490px;width:876px;height:1px;background:#e7eaee}
.footer-info{position:absolute;top:3538px;display:flex;gap:18px}
.footer-info .icon{width:46px;height:46px;border:2px solid var(--blue);border-radius:50%;display:flex;align-items:center;justify-content:center;flex:none}
.footer-info h4{font-size:14px;font-weight:600;color:var(--blue)}
.footer-info p{font-size:14px;line-height:20px;margin-top:6px}
.copyright{position:absolute;left:162px;top:3642px;font-size:13px;font-weight:500}
.social{position:absolute;top:3632px;width:32px;height:32px;border:2px solid var(--blue);border-radius:50%}
.bottom-bar{position:absolute;left:0;top:3675px;width:1200px;height:7px;background:var(--blue)}
</style>
</head>
<body>

<header class="site-header">
  <div class="contact-chip" style="left:160px">
    <svg width="38" height="38" viewBox="0 0 38 38"><circle cx="19" cy="19" r="17" fill="none" stroke="#0f6cc0" stroke-width="2" stroke-dasharray="80 27"/><path d="M14 11c2 0 3 4 2 5l-1 1c1 3 3 5 6 6l1-1c1-1 5 0 5 2s-2 4-4 4c-7-1-12-6-13-13 0-2 2-4 4-4z" fill="#0f6cc0"/></svg>
    <div><div class="label">PHONE:</div><div class="value">(123)456 7890</div></div>
  </div>
  <div class="brand-badge"><span>Palvanor<br>Lending</span></div>
  <div class="contact-chip" style="left:775px">
    <svg width="34" height="30" viewBox="0 0 34 30"><path d="M3 12 17 2l14 10v16H3z" fill="none" stroke="#0f6cc0" stroke-width="2.5" stroke-linejoin="round"/><path d="M3 12l14 10 14-10" fill="none" stroke="#0f6cc0" stroke-width="2.5"/></svg>
    <div><div class="label">EMAIL:</div><div class="value" style="font-size:12px">info@palvanorlending.com</div></div>
  </div>
  <div class="menu-btn" aria-label="Menu"><i style="top:11px"></i><i style="top:16px"></i><i style="top:21px"></i></div>
</header>

<section class="hero">
  <div class="hero-photo" role="img" aria-label="Photo of a father and daughter washing dishes together at a kitchen sink"></div>
  <div class="hero-copy">
    <div class="script">Palvanor Lending</div>
    <h1>Mortgage Brokerage</h1>
    <p>A retail mortgage broker business specially crafted to provide simple, transparent, and comprehensive mortgage solutions</p>
    <div class="btn-pill">CONTACT US <svg width="10" height="10" viewBox="0 0 10 10"><path d="M1 1l4 4-4 4M5 1l4 4-4 4" fill="none" stroke="#fff" stroke-width="1.6"/></svg></div>
  </div>
  <svg class="abs" style="left:0;bottom:0" width="1200" height="110" viewBox="0 0 1200 110">
    <path d="M0 50 C250 -5 450 10 650 55 C850 100 1050 85 1200 78 V110 H0 Z" fill="#fff"/>
    <path d="M0 48 C250 -8 450 8 650 53 C850 98 1050 83 1200 76" fill="none" stroke="#0f6cc0" stroke-width="6"/>
  </svg>
</section>

<h2 class="script-title" style="top:690px">Process</h2>
<div class="title-rule" style="top:757px"></div>

<div class="process-step" style="left:160px">
  <div class="step-visual"><span class="step-num" style="left:34px">1</span>
    <div class="step-ring" style="left:70px"><div class="core">
      <svg width="40" height="48" viewBox="0 0 40 48"><rect x="4" y="6" width="28" height="38" rx="2" fill="none" stroke="#fff" stroke-width="2.5"/><path d="M10 16h16M10 22h16M10 36l6-6 4 3 6-7" fill="none" stroke="#fff" stroke-width="2.2"/><circle cx="32" cy="8" r="7" fill="#0f6cc0" stroke="#fff" stroke-width="2"/></svg>
    </div></div></div>
  <div class="step-label">Financing</div>
</div>
<svg class="abs" style="left:358px;top:835px" width="135" height="40" viewBox="0 0 135 40"><path d="M2 32 C40 0 90 0 122 30" fill="none" stroke="#aaa" stroke-width="1.3" stroke-dasharray="4 4"/><path d="M116 34l10 2-2-10z" fill="#888"/></svg>

<div class="process-step" style="left:480px">
  <div class="step-visual"><span class="step-num" style="left:38px">2</span>
    <div class="step-ring" style="left:76px"><div class="core">
      <svg width="48" height="48" viewBox="0 0 48 48"><path d="M10 24h7v18h-7zM17 40h16c3 0 4-2 4-4l2-10c0-2-1-3-3-3h-9l1-7c0-3-4-4-5-1l-6 9" fill="none" stroke="#fff" stroke-width="2.4" stroke-linejoin="round"/><path d="M14 10l1 3h3l-2 2 1 3-3-2-3 2 1-3-2-2h3zM26 4l1 3h3l-2 2 1 3-3-2-3 2 1-3-2-2h3zM38 10l1 3h3l-2 2 1 3-3-2-3 2 1-3-2-2h3z" fill="#fff"/></svg>
    </div></div></div>
  <div class="step-label">Approval</div>
</div>
<svg class="abs" style="left:690px;top:845px" width="135" height="40" viewBox="0 0 135 40"><path d="M2 8 C40 40 90 40 122 10" fill="none" stroke="#aaa" stroke-width="1.3" stroke-dasharray="4 4"/><path d="M114 8l12-4-2 10z" fill="#888"/></svg>

<div class="process-step" style="left:816px">
  <div class="step-visual"><span class="step-num" style="left:38px">3</span>
    <div class="step-ring" style="left:76px"><div class="core">
      <svg width="44" height="40" viewBox="0 0 44 40"><rect x="4" y="4" width="36" height="32" fill="none" stroke="#fff" stroke-width="2.4"/><path d="M4 12h36M22 17v12M16 24l6 6 6-6" fill="none" stroke="#fff" stroke-width="2.4"/></svg>
    </div></div></div>
  <div class="step-label">Closing</div>
</div>

<section class="products">
  <h2 class="script-title" style="top:60px">Our Products</h2>
  <div class="title-rule" style="top:123px"></div>
  <article class="product-card" style="left:162px">
    <div class="product-photo" role="img" aria-label="Photo of a small model house with keys on a table" style="background:linear-gradient(160deg,#eef0f2,#cfd3d6 60%,#9a9ea2)"></div>
    <h3>Quis nostrud exercitation</h3><div class="rule"></div>
    <p>Lorem ipsum dolor sit amet, conctetur adipiscing elit, sed do eiusmod tempor</p><a>Read More</a>
  </article>
  <article class="product-card" style="left:469px">
    <div class="product-photo" role="img" aria-label="Photo of hands holding a model house over a signed contract" style="background:linear-gradient(160deg,#c9ccd0,#e9e6e0 50%,#b8a48c)"></div>
    <h3>Quis nostrud exercitation</h3><div class="rule"></div>
    <p>Lorem ipsum dolor sit amet, conctetur adipiscing elit, sed do eiusmod tempor</p><a>Read More</a>
  </article>
  <article class="product-card" style="left:776px">
    <div class="product-photo" role="img" aria-label="Photo of a handshake across a desk with a laptop" style="background:linear-gradient(160deg,#5b5149,#a79383 50%,#e6e2dc)"></div>
    <h3>Quis nostrud exercitation</h3><div class="rule"></div>
    <p>Lorem ipsum dolor sit amet, conctetur adipiscing elit, sed do eiusmod tempor</p><a>Read More</a>
  </article>
</section>

<h2 class="script-title" style="top:1695px">Mortgage Calculator</h2>
<div class="title-rule" style="top:1773px"></div>

<section class="calc-card">
  <span class="field-label" style="left:30px;top:36px">Home Price</span>
  <span class="field-value" style="right:393px;top:32px">$3,00,000</span>
  <div class="track" style="top:70px"><div class="fill" style="width:205px"></div><div class="knob" style="left:199px"></div></div>
  <span class="field-label" style="left:30px;top:120px">Down Payment</span>
  <span class="field-value" style="left:275px;top:116px">$45,000</span>
  <span class="field-value" style="left:371px;top:116px;font-size:17px;color:var(--blue)">15%</span>
  <div class="track" style="top:154px"><div class="fill" style="width:145px"></div><div class="knob" style="left:139px"></div></div>
  <span class="field-label" style="left:30px;top:199px">Term Duration</span>
  <span class="field-value" style="left:30px;top:238px">30 Year Fixed</span>
  <svg class="abs" style="left:467px;top:250px" width="14" height="9" viewBox="0 0 14 9"><path d="M1 1l6 6 6-6" fill="none" stroke="#0f6cc0" stroke-width="1.8"/></svg>
  <div class="abs" style="left:30px;top:274px;width:453px;height:1px;background:var(--blue)"></div>
  <div class="calc-divider"></div>
  <div class="payment-ring"><strong>$1,411</strong><span>Month</span></div>
  <ul class="breakdown">
    <li><span>Principal / Interest</span><b>$1,030</b></li>
    <li><span>Property Taxes</span><b>$237</b></li>
    <li><span>Home Insurance</span><b>$114</b></li>
    <li><span>Mortgage Insurance</span><b>$21</b></li>
  </ul>
</section>

<section class="region">
  <div class="region-map" role="img" aria-label="Map of the United States with office region markers in Florida, Texas, Virginia, Maryland and Washington DC"></div>
  <div class="region-panel">
    <h2>We are located in Calverdale MD and our region consists of the following states</h2>
    <ul>
      <li><i></i>Florida</li><li><i></i>Texas</li><li><i></i>Virginia</li><li><i></i>Maryland</li><li><i></i>Washington DC</li>
    </ul>
  </div>
</section>

<h2 class="script-title" style="top:2662px">Customer Reviews</h2>
<div class="title-rule" style="top:2730px"></div>

<section>
  <div class="review-card"></div>
  <div class="abs" style="left:187px;top:2803px;width:403px;height:2px;background:var(--blue-bright)"></div>
  <div class="abs" style="left:874px;top:2760px;font-size:120px;font-weight:700;color:#9cc8ee;line-height:1">&ldquo;</div>
  <div class="review-photo" role="img" aria-label="Portrait photo of a smiling customer"></div>
  <p class="review-quote">&ldquo; Lorem ipsum dolor sit amet, consectetuer adipiscing elit, sed diam nonummy nibh euismod tincidunt ut laoreet dolore magna aliquam erat volutpat. Ut wisi enim ad minim veniam, quis nostrud exerci tation ullamcorper suscipit lobortis nisl ut aliquip ex ea commodo consequat.Lorem ipsum dolor sit amet, consectetuer adipiscing elit, sed diam nonummy nibh euismod tincidunt ut laoreet dolore magna aliquam erat volutpat. Ut wisi enim ad minim veniam, quis nostrud exerci tation ullamcorper suscipit lobortis nisl ut aliquip ex ea commodo consequat.&rdquo;</p>
  <span class="review-author">- John Doe</span>
  <div class="abs" style="left:768px;top:3012px;width:249px;height:2px;background:var(--blue-bright)"></div>
  <div class="dot" style="top:2862px;background:#fff;border:2px solid var(--blue);width:11px;height:11px;left:1067px"></div>
  <div class="dot" style="top:2885px"></div>
  <div class="dot" style="top:2907px"></div>
  <div class="dot" style="top:2930px"></div>
</section>

<section class="cta">
  <p>Do you have an emergency and need to get in touch with us right away? Call us for an immediate response.</p>
  <div class="cta-phone">
    <svg width="18" height="18" viewBox="0 0 18 18"><path d="M5 2c1 0 2 3 1 4l-1 1c1 2 2 4 5 5l1-1c1-1 4 0 4 1s-1 3-3 3C7 15 3 11 2 5c0-2 2-3 3-3z" fill="#0f6cc0"/></svg>
    - 123 456 7890
  </div>
  <svg class="abs" style="left:725px;top:110px" width="125" height="80" viewBox="0 0 125 80"><path d="M120 2 C115 40 80 55 60 48 C45 44 50 28 60 32 C72 36 60 62 35 66 C22 68 12 64 5 60" fill="none" stroke="#fff" stroke-width="1.6"/><path d="M12 54 4 60l10 4" fill="none" stroke="#fff" stroke-width="1.6"/></svg>
</section>

<nav class="footer-nav"><span>HOME</span><span>PRODUCTS</span><span>PROCESS</span><span>ABOUT US</span><span>CONTACT US</span></nav>
<div class="footer-rule"></div>

<div class="footer-info" style="left:160px">
  <div class="icon"><svg width="16" height="22" viewBox="0 0 16 22"><path d="M8 1a7 7 0 0 0-7 7c0 5 7 13 7 13s7-8 7-13a7 7 0 0 0-7-7z" fill="#0f6cc0"/><circle cx="8" cy="8" r="2.6" fill="#fff"/></svg></div>
  <div><h4>Address:</h4><p>123 Building Name, Street Name,<br>City, Country - Zipcode.</p></div>
</div>
<div class="footer-info" style="left:519px">
  <div class="icon"><svg width="16" height="22" viewBox="0 0 16 22"><path d="M8 1a7 7 0 0 0-7 7c0 5 7 13 7 13s7-8 7-13a7 7 0 0 0-7-7z" fill="#0f6cc0"/><circle cx="8" cy="8" r="2.6" fill="#fff"/></svg></div>
  <div><h4>Call Us:</h4><p style="font-size:15px">(123) 456 7890</p></div>
</div>
<div class="footer-info" style="left:818px">
  <div class="icon"><svg width="18" height="14" viewBox="0 0 18 14"><rect x="1" y="1" width="16" height="12" rx="1.5" fill="#0f6cc0"/><path d="M2 2l7 6 7-6" fill="none" stroke="#fff" stroke-width="1.5"/></svg></div>
  <div><h4>Email Us:</h4><p>info@palvanorlending.com</p></div>
</div>

<p class="copyright">Copyright 2020. Palvanor Lending. All Rights Reserved.</p>
<span class="social" style="left:923px"></span>
<span class="social" style="left:964px"></span>
<span class="social" style="left:1004px"></span>
<div class="bottom-bar"></div>

</body>
</html>
```